Web Design Project for lawn care business

after having a logo designed now my website is letting me down.
My websites main purpose is once i have made contact with a customer most will then try to research my company and the work i have done. Going to my unprofessional and untidy site will only put off potential customers. Also some customers will find my site online so must be able to grab their attention.

My site must be in keeping with my logo. Which is modern, sleek and classy. It needs to convey how professional we are and that the customer is getting a professional service.

My existing site will be replaced with the winning design.

Content wise and amount of pages will be similar to mine how ever more data will be inputted by myself.

so far prefer sites designed incorporating links in pictures or animated links to flick through pictures etc

breaks up the site and is more user friendly. 

also need to make sure colours are in keeping with logo or at least have similarities to keep it all uniform.

thanks

Lawn Care

• in keeping font wise with my logo
same colours etc

```html
<!DOCTYPE html>
<html lang="en">
<head>
<meta charset="utf-8">
<title>Fairway Lawn Care – Tree, Garden &amp; Lawn</title>
<link rel="stylesheet" href="https://fonts.googleapis.com/css2?family=Maven+Pro:wght@400;500;700&display=swap">
<style>
  :root {
    --page-bg: #000000;
    --brand-green: #8ad21c;
    --text-green: #5caf22;
    --heading-green: #66b823;
    --nav-top: #a4f01e;
    --nav-bottom: #5fc90a;
    --nav-active: #4fa710;
    --footer-green: #9be81f;
    --footer-text: #1a2a06;
    --card-white: #ffffff;
    --dot-white: #ffffff;
    --grass-light: #7fe23a;
    --grass-dark: #3fa81a;
  }
  * { box-sizing: border-box; margin: 0; padding: 0; }
  html, body { width: 1200px; height: 1000px; overflow: hidden; }
  body {
    position: relative;
    background: var(--page-bg);
    font-family: "Maven Pro", Arial, sans-serif;
    color: var(--text-green);
  }

  /* Brand */
  .brand { position: absolute; left: 66px; top: 38px; display: flex; align-items: center; gap: 18px; }
  .brand-dot { width: 88px; height: 88px; border-radius: 50%; background: var(--card-white); }
  .brand-text { color: var(--brand-green); font-weight: 500; }
  .brand-name { font-size: 36px; line-height: 40px; letter-spacing: 1px; }
  .brand-sub { font-size: 22px; line-height: 26px; letter-spacing: 1px; color: #ffffff; }
  .brand-tag { font-size: 11px; line-height: 14px; letter-spacing: .5px; font-weight: 700; }

  /* Main navigation */
  .main-nav {
    position: absolute; left: 220px; top: 138px; width: 908px; height: 43px;
    border-radius: 8px;
    background: linear-gradient(to bottom, var(--nav-top), var(--nav-bottom));
    display: flex; align-items: center; justify-content: space-between;
    padding: 0 12px 0 10px;
  }
  .main-nav a {
    color: #ffffff; text-decoration: none; font-size: 18px; letter-spacing: .4px;
    padding: 5px 10px; border-radius: 6px;
  }
  .main-nav a.is-active { background: var(--nav-active); }

  /* Slideshow */
  .slideshow {
    position: absolute; left: 90px; top: 278px; width: 418px; height: 260px;
    background: var(--card-white); padding: 5px; border-radius: 3px;
  }
  .slide {
    width: 100%; height: 100%; border-radius: 10px;
    background: radial-gradient(ellipse at 40% 40%, var(--grass-light), var(--grass-dark));
  }
  .slide-dots { position: absolute; left: 216px; top: 560px; display: flex; gap: 12px; }
  .slide-dots span { width: 19px; height: 19px; border-radius: 50%; background: var(--dot-white); }
  .slide-dots span.is-current { background: var(--brand-green); }

  /* Quote box */
  .quote-box {
    position: absolute; left: 88px; top: 634px; width: 418px; height: 211px;
    background: var(--card-white); border-radius: 12px; text-align: center;
    padding-top: 32px;
  }
  .quote-lead { color: var(--brand-green); font-size: 20px; line-height: 22px; }
  .quote-name { color: var(--brand-green); font-size: 24px; font-weight: 700; margin-top: 20px; letter-spacing: 1px; }
  .quote-contact { color: var(--brand-green); font-size: 18px; font-weight: 700; line-height: 27px; letter-spacing: .4px; }

  /* Intro card */
  .intro-card {
    position: absolute; left: 562px; top: 240px; width: 566px; height: 647px;
    background: var(--card-white); border-radius: 16px;
    padding: 26px 56px 0 41px;
  }
  .intro-title {
    color: var(--heading-green); font-weight: 400; font-size: 28px; line-height: 38px;
    letter-spacing: .8px; padding-left: 9px; margin-bottom: 17px; white-space: nowrap;
  }
  .intro-card p { font-size: 15px; line-height: 21px; letter-spacing: .3px; }
  .intro-card p + p { margin-top: 21px; }

  /* Footer */
  .site-footer {
    position: absolute; left: 87px; top: 941px; width: 1037px; height: 33px;
    background: var(--footer-green); border-radius: 8px;
    display: flex; align-items: center; padding-left: 57px;
    font-size: 12px; font-weight: 500; letter-spacing: .6px; color: var(--footer-text);
  }
  .footer-nav { display: flex; gap: 30px; }
  .footer-nav a { color: var(--footer-text); text-decoration: none; }
  .copyright { margin-left: 55px; }
  .share { display: flex; gap: 6px; margin-left: 40px; }
  .share span {
    background: #ffffff; color: #33557a; font-size: 8px; font-weight: 700;
    padding: 2px 4px; border-radius: 2px; line-height: 10px;
  }
</style>
</head>
<body>

<header class="brand">
  <div class="brand-dot"></div>
  <div class="brand-text">
    <div class="brand-name">FAIRWAY</div>
    <div class="brand-sub">LAWN CARE</div>
    <div class="brand-tag">TREE, GARDEN &amp; LAWN</div>
  </div>
</header>

<nav class="main-nav">
  <a href="#" class="is-active">HOME</a>
  <a href="#">CONTACT US</a>
  <a href="#">OUR SERVICES</a>
  <a href="#">USEFUL LINKS</a>
  <a href="#">LAWNCARE ADVICE</a>
  <a href="#">FAQS</a>
</nav>

<section class="slideshow">
  <div class="slide" role="img" aria-label="Photograph of a close-cut green lawn"></div>
</section>
<div class="slide-dots">
  <span></span><span class="is-current"></span><span></span><span></span><span></span><span></span>
</div>

<aside class="quote-box">
  <p class="quote-lead">Please contact us for a<br>free no obligation quote</p>
  <p class="quote-name">MARTIN</p>
  <p class="quote-contact">07700 900 214<br>martin@fairwaylawns.example</p>
</aside>

<main class="intro-card">
  <h1 class="intro-title">FAIRWAY LAWN CARE<br>TREE GARDEN &amp; LAWN SERVICES</h1>
  <p>All of our work is carried out by fully trained turf professionals, so why do it yourself?<br>
  &nbsp;As turf specialists, the careful attention to detail and passion that goes into caring for a golf course also goes into every job, from general mowing to full hard landscaping jobs and everything in between.<br>
  Everybody knows that golf greens are the most pristine, well kept and visually pleasing grassed areas anywhere. With this in mind, who else would you want maintaining, renovating and building your own garden?</p>
  <p>With access to every piece of equipment, material, treatment and staff needed to look after a golf course, we can offer you the very same services tailored to your garden, no matter how big or small, at a fair price that costs less than DIY methods with inefficient materials. All of our staff are fully qualified with at least a national diploma in sports turf, a two year course covering both practical work and theory. Every member of the team also holds recognised spraying certificates, which allow us to apply treatments that most gardeners or home users cannot even get hold of. All staff also carry the relevant chainsaw certificates for any tree care needs.</p>
  <p>Please contact us for a free no obligation quote</p>
</main>

<footer class="site-footer">
  <nav class="footer-nav">
    <a href="#">HOME</a>
    <a href="#">CONTACT US</a>
    <a href="#">OUR SERVICES</a>
    <a href="#">USEFUL LINKS</a>
    <a href="#">LAWNCARE ADVICE</a>
    <a href="#">FAQS</a>
  </nav>
  <span class="copyright">All rights reserved 2013</span>
  <div class="share"><span>Post</span><span>Like</span><span>+1</span></div>
</footer>

</body>
</html>
```